Skin care manufacturer looking for packaging design for new skin care brand.

We need a design and logo for a skin care brand to be sold at retail stores and online in the United States and Europe. The design will be for 1.7oz - 2oz serums that will not have a retail box. The name of the brand is Velora Fen and should be a luxurious brand that is approachable. The brand will consist of 4 face serums - Vitamin C, Collagen, Retinol and Hyaluronic Acid that all contain Dead Sea Minerals. Images shown are for inspiration only. Color of bottles can be varied based on design and bottles can be screen printed or labeled.

```html
<!DOCTYPE html>
<html lang="en">
<head>
<meta charset="utf-8">
<title>Velora Fen Facial Serums</title>
<link rel="stylesheet" href="https://fonts.googleapis.com/css2?family=Bodoni+Moda:wght@400&family=Montserrat:wght@400;600&display=swap">
<style>
  :root {
    --bg: #ececec;
    --ink: #ffffff;
    --cap: #c9a982;
    --cap-dark: #6b4a33;
    --bulb: #f4f4f4;
    --violet-top: #a65cf6;
    --violet-mid: #c443dc;
    --violet-low: #7f2c78;
    --blue-top: #3f9fe6;
    --blue-mid: #2477c9;
    --blue-low: #1d4a70;
    --amber-top: #f1b530;
    --amber-mid: #e2701c;
    --amber-low: #74380f;
    --ruby-top: #ec4a5a;
    --ruby-mid: #cf2b34;
    --ruby-low: #742029;
  }
  html, body { margin: 0; padding: 0; overflow: hidden; }
  body { width: 1200px; height: 856px; background: var(--bg); }
  .lineup { display: block; width: 1200px; height: 856px; }
  .wordmark { font-family: "Bodoni Moda", serif; font-weight: 400; fill: var(--ink); }
  .range { font-family: "Bodoni Moda", serif; font-weight: 400; fill: var(--ink); }
  .ingredient { font-family: "Montserrat", sans-serif; font-weight: 600; fill: var(--ink); }
  .detail { font-family: "Montserrat", sans-serif; font-weight: 400; fill: var(--ink); }
  .pill { fill: none; stroke: var(--ink); stroke-width: 1; }
  .rule { stroke: var(--ink); stroke-width: 0.6; }
  .cap { fill: var(--cap); }
  .cap-shade { fill: var(--cap-dark); opacity: .55; }
  .bulb { fill: var(--bulb); }
</style>
</head>
<body>
<svg class="lineup" viewBox="0 0 1200 856" xmlns="http://www.w3.org/2000/svg">
  <defs>
    <linearGradient id="violet" x1="0" y1="0" x2="0" y2="1">
      <stop offset="0" stop-color="var(--violet-top)"/>
      <stop offset=".6" stop-color="var(--violet-mid)"/>
      <stop offset="1" stop-color="var(--violet-low)"/>
    </linearGradient>
    <linearGradient id="blue" x1="0" y1="0" x2="0" y2="1">
      <stop offset="0" stop-color="var(--blue-top)"/>
      <stop offset=".6" stop-color="var(--blue-mid)"/>
      <stop offset="1" stop-color="var(--blue-low)"/>
    </linearGradient>
    <linearGradient id="amber" x1="0" y1="0" x2="0" y2="1">
      <stop offset="0" stop-color="var(--amber-top)"/>
      <stop offset=".6" stop-color="var(--amber-mid)"/>
      <stop offset="1" stop-color="var(--amber-low)"/>
    </linearGradient>
    <linearGradient id="ruby" x1="0" y1="0" x2="0" y2="1">
      <stop offset="0" stop-color="var(--ruby-top)"/>
      <stop offset=".6" stop-color="var(--ruby-mid)"/>
      <stop offset="1" stop-color="var(--ruby-low)"/>
    </linearGradient>
  </defs>

  <!-- Collagen -->
  <g class="bottle" transform="translate(84,0)">
    <path class="bulb" d="M80 218 V100 a38 38 0 0 1 76 0 V218 Z"/>
    <rect class="cap" x="40" y="218" width="156" height="125" rx="3"/>
    <rect class="cap-shade" x="100" y="218" width="36" height="125"/>
    <rect x="0" y="343" width="237" height="402" rx="14" fill="url(#violet)"/>
    <text class="wordmark" transform="translate(68,712) rotate(-90)" font-size="68" textLength="334" lengthAdjust="spacingAndGlyphs">VELORA FEN</text>
    <rect class="pill" x="103" y="514" width="115" height="24" rx="12"/>
    <text class="ingredient" x="160.5" y="532" font-size="17" text-anchor="middle">• Collagen</text>
    <text class="range" x="105" y="662" font-size="17">FACIAL</text>
    <text class="range" x="105" y="677" font-size="17">SERUMS</text>
    <text class="detail" x="105" y="684" font-size="6">With</text>
    <line class="rule" x1="121" y1="682" x2="172" y2="682"/>
    <text class="detail" x="105" y="693" font-size="8">Dead Sea Minerals</text>
    <text class="detail" x="105" y="712" font-size="8.5">1.7 FL. oz. (50ml)</text>
  </g>

  <!-- Hyaluronic Acid -->
  <g class="bottle" transform="translate(347,0)">
    <path class="bulb" d="M80 218 V100 a38 38 0 0 1 76 0 V218 Z"/>
    <rect class="cap" x="40" y="218" width="156" height="125" rx="3"/>
    <rect class="cap-shade" x="100" y="218" width="36" height="125"/>
    <rect x="0" y="343" width="237" height="402" rx="14" fill="url(#blue)"/>
    <text class="wordmark" transform="translate(68,712) rotate(-90)" font-size="68" textLength="334" lengthAdjust="spacingAndGlyphs">VELORA FEN</text>
    <rect class="pill" x="103" y="514" width="115" height="24" rx="12"/>
    <text class="ingredient" x="160.5" y="530" font-size="11" text-anchor="middle">• Hyaluronic Acid</text>
    <text class="range" x="105" y="662" font-size="17">FACIAL</text>
    <text class="range" x="105" y="677" font-size="17">SERUMS</text>
    <text class="detail" x="105" y="684" font-size="6">With</text>
    <line class="rule" x1="121" y1="682" x2="172" y2="682"/>
    <text class="detail" x="105" y="693" font-size="8">Dead Sea Minerals</text>
    <text class="detail" x="105" y="712" font-size="8.5">1.7 FL. oz. (50ml)</text>
  </g>

  <!-- Vitamin C -->
  <g class="bottle" transform="translate(610,0)">
    <path class="bulb" d="M80 218 V100 a38 38 0 0 1 76 0 V218 Z"/>
    <rect class="cap" x="40" y="218" width="156" height="125" rx="3"/>
    <rect class="cap-shade" x="100" y="218" width="36" height="125"/>
    <rect x="0" y="343" width="237" height="402" rx="14" fill="url(#amber)"/>
    <text class="wordmark" transform="translate(68,712) rotate(-90)" font-size="68" textLength="334" lengthAdjust="spacingAndGlyphs">VELORA FEN</text>
    <rect class="pill" x="103" y="514" width="115" height="24" rx="12"/>
    <text class="ingredient" x="160.5" y="532" font-size="17" text-anchor="middle">• Vitamin C</text>
    <text class="range" x="105" y="662" font-size="17">FACIAL</text>
    <text class="range" x="105" y="677" font-size="17">SERUMS</text>
    <text class="detail" x="105" y="684" font-size="6">With</text>
    <line class="rule" x1="121" y1="682" x2="172" y2="682"/>
    <text class="detail" x="105" y="693" font-size="8">Dead Sea Minerals</text>
    <text class="detail" x="105" y="712" font-size="8.5">1.7 FL. oz. (50ml)</text>
  </g>

  <!-- Retinol -->
  <g class="bottle" transform="translate(873,0)">
    <path class="bulb" d="M80 218 V100 a38 38 0 0 1 76 0 V218 Z"/>
    <rect class="cap" x="40" y="218" width="156" height="125" rx="3"/>
    <rect class="cap-shade" x="100" y="218" width="36" height="125"/>
    <rect x="0" y="343" width="237" height="402" rx="14" fill="url(#ruby)"/>
    <text class="wordmark" transform="translate(68,712) rotate(-90)" font-size="68" textLength="334" lengthAdjust="spacingAndGlyphs">VELORA FEN</text>
    <rect class="pill" x="103" y="514" width="115" height="24" rx="12"/>
    <text class="ingredient" x="160.5" y="532" font-size="17" text-anchor="middle">• Retinol</text>
    <text class="range" x="105" y="662" font-size="17">FACIAL</text>
    <text class="range" x="105" y="677" font-size="17">SERUMS</text>
    <text class="detail" x="105" y="684" font-size="6">With</text>
    <line class="rule" x1="121" y1="682" x2="172" y2="682"/>
    <text class="detail" x="105" y="693" font-size="8">Dead Sea Minerals</text>
    <text class="detail" x="105" y="712" font-size="8.5">1.7 FL. oz. (50ml)</text>
  </g>
</svg>
</body>
</html>
```